" Comprei equipamentos para produção de cervejas, próprias e para terceiros. As chamadas cervejarias ciganas termo que se refere as cervejarias que produzem cervejas para outras pessoas e/ou empresas. "

```html
<!DOCTYPE html>
<html lang="pt-BR">
<head>
<meta charset="UTF-8">
<title>Serralta Pilsen – Rótulo</title>
<link rel="stylesheet" href="https://fonts.googleapis.com/css2?family=Open+Sans:wght@400;600;700&display=swap">
<style>
  :root{
    --bg-light:#fffdf2;
    --bg-warm:#f3eed2;
    --green-dark:#14301f;
    --green-mid:#234a31;
    --gold:#c9a54e;
    --gold-light:#e8cf86;
    --gold-deep:#9c7c34;
    --white:#ffffff;
    --ink-label:#a88a3f;
  }
  *{margin:0;padding:0;box-sizing:border-box}
  html,body{width:1200px;height:1200px;overflow:hidden}
  body{
    background:radial-gradient(circle at 50% 45%,var(--bg-light) 0%,var(--bg-light) 45%,var(--bg-warm) 100%);
    font-family:"Open Sans",Arial,sans-serif;
    position:relative;
  }
  .label-shape{position:absolute;left:0;top:0;width:1200px;height:1200px}
  .line{
    position:absolute;left:0;width:1200px;text-align:center;
    color:var(--white);font-size:24px;line-height:1.2;
  }
  .category{top:166px;font-size:31px;letter-spacing:14px;text-indent:14px;font-weight:600}
  .brand-name{top:248px;font-size:92px;font-weight:700;color:var(--gold-light);letter-spacing:1px;line-height:1}
  .brand-variant{top:350px;left:120px;font-size:40px;font-weight:700;color:var(--gold-light);line-height:1}
  .tagline{top:408px;font-size:28px;color:var(--gold-light)}
  .gold{color:var(--gold-light)}
  .bold{font-weight:700}
  .info-box{
    position:absolute;left:355px;top:944px;width:494px;height:93px;
    background:var(--white);border-radius:14px;
    padding:17px 22px;color:var(--ink-label);font-weight:700;font-size:23px;line-height:34px;
  }
</style>
</head>
<body>
  <svg class="label-shape" viewBox="0 0 1200 1200" aria-hidden="true">
    <defs>
      <linearGradient id="rim" x1="0" y1="0" x2="1" y2="1">
        <stop offset="0" stop-color="#f3dc93"/>
        <stop offset="0.5" stop-color="#b8913c"/>
        <stop offset="1" stop-color="#e6c97a"/>
      </linearGradient>
      <radialGradient id="field" cx="0.5" cy="0.25" r="0.9">
        <stop offset="0" stop-color="#2b5639"/>
        <stop offset="1" stop-color="#14301f"/>
      </radialGradient>
    </defs>
    <path fill="url(#rim)" d="M352 122 H848 Q886 122 886 160 Q852 600 886 1040 Q886 1078 848 1078 H352 Q314 1078 314 1040 Q348 600 314 160 Q314 122 352 122 Z"/>
    <path fill="url(#field)" role="img" aria-label="Fundo verde com raios em tons de verde" d="M356 134 H844 Q874 134 874 164 Q840 600 874 1036 Q874 1066 844 1066 H356 Q326 1066 326 1036 Q360 600 326 164 Q326 134 356 134 Z"/>
  </svg>

  <div class="line category">CERVEJAS</div>
  <div class="line brand-name">Serralta</div>
  <div class="line brand-variant">Pilsen</div>
  <div class="line tagline">Cervejas feitas à mão.</div>

  <div class="line gold bold" style="top:482px">Composição:</div>
  <div class="line" style="top:515px">Malte, Água, Lúpulo e Levedura.</div>
  <div class="line" style="top:548px">CONTÉM GLÚTEN.</div>
  <div class="line" style="top:581px">Teor Alcóolico: 4,7%</div>
  <div class="line" style="top:614px">IBU: 120</div>

  <div class="line" style="top:660px">Fabricado e engarrafado por Serralta</div>
  <div class="line" style="top:694px">Cervejas; CNPJ: 00.000.000/0000-00</div>
  <div class="line" style="top:728px">Rua das Palmeiras, 850, Centro,</div>
  <div class="line" style="top:762px">Serralta/MG - CEP: 37480-000</div>

  <div class="line gold" style="top:802px">Produto destinado a adultos.</div>
  <div class="line bold" style="top:843px">Se beber, Não dirija.</div>
  <div class="line" style="top:899px"><span class="gold">Validade:</span> 06 meses</div>

  <div class="info-box">
    <div>Data de Fabricação:</div>
    <div>Lote de Fab.:</div>
  </div>
</body>
</html>
```